5 Banner für die Startseite der Hompage
Zielgruppe
Wir sind eine 'kreative' kleine Truppe, die mit neuen Ideen versuchen wollen, auch mal andere Wege in den Projekten zu gehen.
unsere neue Webseite lautet
Aufgabenstellung
Auf meiner Webseite www.kavelorn.de habe ich bereits einen ersten Vorschlag eingefügt.
Es geht um die 5 Banner auf der Startseite; diese sollen sowohl Designtechnisch als auch optisch sehr ansprechend wirken, um das Interesse potentieller Kunden zu wecken.
Meine Farben habe ich mit angehängt.
Der Text könnte sich noch anpassen, muss aber mit in den Banner aufgenommen werden.
Breite sollte 1200Pixel; Höhe 600Pixel

```html
<!DOCTYPE html>
<html lang="de">
<head>
<meta charset="utf-8">
<title>Kavelorn – Startseiten-Banner</title>
<link rel="stylesheet" href="https://fonts.googleapis.com/css2?family=Jost:wght@400;500;600&family=Oswald:wght@500;600&display=swap">
<style>
:root{
  --coral:#e8626c;
  --ink:#3b3f41;
  --ink-deep:#2d3032;
  --ink-soft:#4d5254;
  --text-light:#e4e5e6;
  --text-dim:#b9bcbe;
  --paper:#ffffff;
  --rule:#d9d9d9;
  --rose:#8e5f5a;
  --rose-soft:#b0837c;
  --body:#4a4a4a;
}
*{box-sizing:border-box;margin:0;padding:0}
html,body{width:1200px;height:3343px;overflow:hidden;background:var(--paper)}
body{position:relative;font-family:"Jost",sans-serif}

/* ---------- Website preview ---------- */
.site{position:absolute;left:127px;top:100px;width:946px;height:600px;overflow:hidden;background:var(--paper);box-shadow:0 0 0 1px var(--rule)}
.site__hero{position:absolute;left:0;top:0;width:946px;height:400px;
  background:
    radial-gradient(ellipse 380px 260px at 20% 70%,rgba(60,35,33,.55),rgba(60,35,33,0)),
    radial-gradient(ellipse 300px 220px at 88% 30%,rgba(210,170,160,.45),rgba(210,170,160,0)),
    linear-gradient(135deg,#a9766e,var(--rose) 45%,#5e3c38)}
.site__nav{position:absolute;left:0;top:0;width:100%;height:40px;display:flex;align-items:center;justify-content:space-between;padding:0 160px 0 130px}
.site__brand{font-weight:600;font-size:15px;color:var(--paper);display:flex;align-items:center;gap:6px}
.site__brand i{width:7px;height:7px;background:var(--coral);border-radius:50%;display:block}
.site__menu{display:flex;gap:14px;list-style:none;font-size:9px;font-weight:500;color:var(--paper)}
.hero-card{position:absolute;left:129px;top:66px;width:644px;height:324px;overflow:hidden;background:radial-gradient(circle at 80% 60%,var(--ink-soft),var(--ink-deep))}
.hero-card__photo{position:absolute;left:0;top:0;width:360px;height:100%;
  background:
    radial-gradient(ellipse 90px 110px at 52% 40%,#d9d9d9,rgba(217,217,217,0) 100%),
    radial-gradient(ellipse 150px 110px at 45% 20%,rgba(240,240,240,.75),rgba(240,240,240,0)),
    radial-gradient(ellipse 170px 120px at 45% 95%,#1e1f20,rgba(30,31,32,0)),
    linear-gradient(180deg,#777,#4a4c4d);
  -webkit-mask-image:linear-gradient(90deg,#000 65%,transparent);mask-image:linear-gradient(90deg,#000 65%,transparent)}
.hero-card .quote{left:330px;top:28px;width:250px;padding:16px 14px 12px 18px;border-width:1.5px}
.hero-card .quote__text{font-size:19px;line-height:1.15}
.hero-card .quote__source{font-size:6px;margin-top:4px}
.hero-card .quote__mark{left:10px;top:-11px;width:18px}
.hero-card .quote__tail{width:16px;height:14px;bottom:-14px}
.hero-card .lead{left:330px;top:212px;width:290px;font-size:11px;line-height:1.7}
.hero-card .cta{right:22px;bottom:18px;font-size:11px}
.hero-card .cta__ring{width:14px;height:14px;border-width:3px}

.site__section{position:absolute;left:0;top:400px;width:100%;height:200px}
.section__title{position:absolute;top:56px;width:100%;text-align:center;font-family:"Oswald",sans-serif;font-weight:600;font-size:27px;color:#3a3a3a;letter-spacing:.5px}
.section__marks{position:absolute;top:96px;width:100%;text-align:center;font-size:12px;color:#3a3a3a;letter-spacing:6px}
.section__col{position:absolute;top:130px;width:300px;font-size:9px;line-height:1.75;color:var(--body)}
.section__col--left{left:129px}
.section__col--right{left:460px}
.dropcap{float:left;width:30px;height:30px;border:1.5px solid #3a3a3a;margin:2px 7px 0 0;font-family:"Oswald",sans-serif;font-size:18px;text-align:center;line-height:27px;color:#3a3a3a}

/* ---------- Banners ---------- */
.banner{position:absolute;left:95px;width:1010px;height:506px;overflow:hidden;background:radial-gradient(circle at 78% 62%,var(--ink-soft),var(--ink-deep) 75%)}
.banner--learn{top:1025px}
.banner--gears{top:1586px}
.banner--ceo{top:2146px}
.banner--product{top:2702px}
.banner__rings{position:absolute;inset:0}
.banner__photo{position:absolute;left:0;top:0;height:100%;width:640px;
  -webkit-mask-image:linear-gradient(90deg,#000 62%,transparent 98%);mask-image:linear-gradient(90deg,#000 62%,transparent 98%)}
.banner--learn .banner__photo{background:
  radial-gradient(ellipse 130px 120px at 38% 26%,#c9c9c9,rgba(201,201,201,0)),
  radial-gradient(ellipse 120px 150px at 37% 72%,#1c1d1e,rgba(28,29,30,0)),
  radial-gradient(ellipse 170px 230px at 10% 50%,#8e9294,rgba(142,146,148,0)),
  radial-gradient(ellipse 200px 160px at 80% 20%,#6e7274,rgba(110,114,116,0)),
  linear-gradient(180deg,#5b5f61,#3e4244)}
.banner--gears .banner__photo{background:
  radial-gradient(ellipse 170px 120px at 18% 14%,#e2e2e2,rgba(226,226,226,0)),
  radial-gradient(ellipse 190px 150px at 30% 64%,#b3b5b6,rgba(179,181,182,0)),
  radial-gradient(ellipse 130px 110px at 70% 78%,#5d6061,rgba(93,96,97,0)),
  radial-gradient(ellipse 110px 90px at 8% 92%,#2f3132,rgba(47,49,50,0)),
  radial-gradient(ellipse 160px 140px at 62% 30%,#8d8f90,rgba(141,143,144,0)),
  linear-gradient(180deg,#7b7d7e,#4a4d4f)}
.banner--ceo .banner__photo{background:
  radial-gradient(ellipse 80px 100px at 19% 24%,#d0d0d0,rgba(208,208,208,0)),
  radial-gradient(ellipse 160px 150px at 22% 82%,#3a3c3d,rgba(58,60,61,0)),
  radial-gradient(ellipse 90px 120px at 52% 35%,#5d6062,rgba(93,96,98,0)),
  radial-gradient(ellipse 200px 150px at 40% 12%,#aeb0b1,rgba(174,176,177,0)),
  linear-gradient(180deg,#8a8c8d,#55585a)}
.banner--product .banner__photo{background:
  radial-gradient(ellipse 150px 80px at 35% 64%,#f2f2f2,rgba(242,242,242,0)),
  radial-gradient(ellipse 110px 60px at 50% 14%,#ececec,rgba(236,236,236,0)),
  radial-gradient(ellipse 140px 130px at 10% 22%,#cfcfcf,rgba(207,207,207,0)),
  radial-gradient(ellipse 180px 110px at 28% 95%,#6a6d6e,rgba(106,109,110,0)),
  linear-gradient(180deg,#b3b5b6,#7d8081)}

.quote{position:absolute;left:522px;top:40px;width:459px;border:2px solid var(--coral);padding:28px 28px 20px 28px}
.quote__mark{position:absolute;left:20px;top:-18px;width:30px}
.quote__tail{position:absolute;left:-2px;bottom:-26px;width:28px;height:26px}
.quote__text{font-weight:500;font-size:30px;line-height:1.2;color:#fff}
.quote__source{font-size:9px;font-style:italic;color:var(--text-dim);text-align:right;margin-top:8px}

.lead{position:absolute;left:522px;width:420px;font-size:15.5px;line-height:1.9;color:var(--text-light);letter-spacing:.3px}
.cta{position:absolute;right:36px;bottom:48px;display:flex;align-items:center;gap:12px;font-size:17px;font-weight:600;color:var(--coral)}
.cta__ring{width:22px;height:22px;border:5px solid var(--coral);border-radius:50%}
</style>
</head>
<body>

<section class="site">
  <div class="site__hero" role="img" aria-label="Rosa getönter Hintergrund mit technischen Rasterlinien">
    <nav class="site__nav">
      <div class="site__brand"><i></i>Kavelorn</div>
      <ul class="site__menu"><li>Home</li><li>Unser Ansatz</li><li>Produkte</li><li>Dienstleistungen</li><li>Schulungen</li></ul>
    </nav>
  </div>
  <div class="hero-card">
    <div class="hero-card__photo" role="img" aria-label="Schwarzweißporträt eines älteren Wissenschaftlers"></div>
    <div class="quote">
      <svg class="quote__mark" viewBox="0 0 30 22"><path d="M6 0h9l-6 22H0zM20 0h9l-6 22h-9z" fill="#e8626c"/></svg>
      <p class="quote__text">Probleme kann man<br>niemals mit derselben<br>Denkweise lösen, durch<br>die sie entstanden sind.“</p>
      <p class="quote__source">Konrad Felsmann</p>
      <svg class="quote__tail" viewBox="0 0 28 26"><path d="M1 0V25L26 1" fill="#3b3f41" stroke="#e8626c" stroke-width="2"/></svg>
    </div>
    <p class="lead">Die Komplexität Ihrer Systeme ist zum Haare raufen? Sie wollen Probleme und Risiken schneller identifizieren und lösen? Dann sind Sie bei uns richtig!</p>
    <div class="cta">Jetzt mehr erfahren <span class="cta__ring"></span></div>
  </div>
  <div class="site__section">
    <h2 class="section__title">UNSER ANSATZ</h2>
    <div class="section__marks">× × ×</div>
    <p class="section__col section__col--left"><span class="dropcap">S</span>ystemdiagnostik ist die Lehre und Kunst, die das Stellen von Diagnosen für Systeme zum Gegenstand hat. Alle Methoden, Verfahren, Prozesse und Anwendungen, die für die Ermittlung und Ableitung der Symptome eines Fehlverhaltens und der Identifikation von Ursachen notwendig sind, gehören dazu.</p>
    <p class="section__col section__col--right">Systemdiagnostik ist unsere Leidenschaft. Seit dem Jahr 2000 beschäftigen wir uns mit der Fragestellung „Wie muss ein System und deren interne und externe Komponenten entwickelt werden, sodass es genügend Eigenintelligenz zur Fehlerdiagnose besitzt?“ Die Antwort muss nicht kompliziert sein.</p>
  </div>
</section>

<section class="banner banner--learn">
  <svg class="banner__rings" viewBox="0 0 1010 506"><circle cx="760" cy="330" r="300" fill="#fff" fill-opacity=".03"/><circle cx="930" cy="120" r="200" fill="#fff" fill-opacity=".03"/></svg>
  <div class="banner__photo" role="img" aria-label="Kind mit wilden Locken und verschränkten Armen vor einer Tafel voller Formeln"></div>
  <div class="quote">
    <svg class="quote__mark" viewBox="0 0 30 22"><path d="M6 0h9l-6 22H0zM20 0h9l-6 22h-9z" fill="#e8626c"/></svg>
    <p class="quote__text">Was men lernen muss,<br>um es zu tun, das lernt man,<br>indem man es tut.“</p>
    <p class="quote__source">Demetrios Kallias</p>
    <svg class="quote__tail" viewBox="0 0 28 26"><path d="M1 0V25L26 1" fill="#3b3f41" stroke="#e8626c" stroke-width="2"/></svg>
  </div>
  <p class="lead" style="top:284px">Unsere Schulungen sind an Ihren Themen und Anwendungen ausgerichtet. Besonders liegen uns Konzepte am Herzen, die Sie in Ihrer Arbeit begleiten.</p>
  <div class="cta">Jetzt mehr erfahren <span class="cta__ring"></span></div>
</section>

<section class="banner banner--gears">
  <svg class="banner__rings" viewBox="0 0 1010 506"><circle cx="760" cy="330" r="300" fill="#fff" fill-opacity=".03"/><circle cx="930" cy="120" r="200" fill="#fff" fill-opacity=".03"/></svg>
  <div class="banner__photo" role="img" aria-label="Ineinandergreifende Zahnräder aus Metall"></div>
  <div class="quote" style="top:44px">
    <svg class="quote__mark" viewBox="0 0 30 22"><path d="M6 0h9l-6 22H0zM20 0h9l-6 22h-9z" fill="#e8626c"/></svg>
    <p class="quote__text">Wir sind erfolgreich,<br>weil wir ganz<br>gewöhnliche Dinge,<br>außergewöhnlich tun.“</p>
    <p class="quote__source">Ruedi Amsler / Schweizer Unternehmer &amp; Gründer von Lindenhof</p>
    <svg class="quote__tail" viewBox="0 0 28 26"><path d="M1 0V25L26 1" fill="#3b3f41" stroke="#e8626c" stroke-width="2"/></svg>
  </div>
  <p class="lead" style="top:300px;width:440px">Abhängig davon, was Sie wirklich brauchen, beraten wir Sie zu unseren Methoden, führen diese bei Ihnen ein, begleiten Ihre Projekte oder übernehmen die komplette Projektverantwortung.</p>
  <div class="cta">Jetzt mehr erfahren <span class="cta__ring"></span></div>
</section>

<section class="banner banner--ceo">
  <svg class="banner__rings" viewBox="0 0 1010 506"><circle cx="760" cy="330" r="300" fill="#fff" fill-opacity=".03"/><circle cx="930" cy="120" r="200" fill="#fff" fill-opacity=".03"/></svg>
  <div class="banner__photo" role="img" aria-label="Lächelnder Mann mit Brille im Büro, Kollege im Hintergrund"></div>
  <div class="quote" style="top:44px">
    <svg class="quote__mark" viewBox="0 0 30 22"><path d="M6 0h9l-6 22H0zM20 0h9l-6 22h-9z" fill="#e8626c"/></svg>
    <p class="quote__text">Systemdiagnostik<br>ist unsere Leidenschaft.“</p>
    <p class="quote__source">Wulf Kamper / CEO Kavelorn</p>
    <svg class="quote__tail" viewBox="0 0 28 26"><path d="M1 0V25L26 1" fill="#3b3f41" stroke="#e8626c" stroke-width="2"/></svg>
  </div>
  <p class="lead" style="top:238px">Unsere Erfahrungen sind ganz klar:<br>die Lösung, die Sie suchen, darf die Komplexität nicht zusätzlich erhöhen. Sie muss EINFACH sein.</p>
  <div class="cta">Jetzt mehr erfahren <span class="cta__ring"></span></div>
</section>

<section class="banner banner--product">
  <svg class="banner__rings" viewBox="0 0 1010 506"><circle cx="760" cy="330" r="300" fill="#fff" fill-opacity=".03"/><circle cx="930" cy="120" r="200" fill="#fff" fill-opacity=".03"/></svg>
  <div class="banner__photo" role="img" aria-label="Hände halten Produktschachteln und Unterlagen"></div>
  <div class="quote" style="top:44px">
    <svg class="quote__mark" viewBox="0 0 30 22"><path d="M6 0h9l-6 22H0zM20 0h9l-6 22h-9z" fill="#e8626c"/></svg>
    <p class="quote__text">Es gibt eine Möglichkeit,<br>es besser zu machen –<br>finde sie!“</p>
    <p class="quote__source">Elias Warren Hale</p>
    <svg class="quote__tail" viewBox="0 0 28 26"><path d="M1 0V25L26 1" fill="#3b3f41" stroke="#e8626c" stroke-width="2"/></svg>
  </div>
  <p class="lead" style="top:284px;width:440px">Mit den Kavelorn-Produktion werden Sie durch unsere Methoden geführt. Sie betrachten Ihre Systeme vollständig und strukturiert, Ihr einmal erarbeitetes Wissen bleibt elektronisch verfügbar und wiederverwendbar.</p>
  <div class="cta" style="bottom:36px">Jetzt mehr erfahren <span class="cta__ring"></span></div>
</section>

</body>
</html>
```